Construction Company informative web page

Torvell Builders is a new company that combine Project Manager and kitchen & bath design with Interior remodeling for houses or business (commercial and residential construction)
We want to show our reviews, portafolio and background experience
Updates

Reason: I would like to have the time to interact with the favorite designers to fine tune the website also I'd like to see more designs

Hello Everybody,

Thank you for your time, please make the corrections shown below:

Pages:

1. Home:

1.  Includes a welcome and a briefly background:

2. Right side vertically show a few reviews with the option read more to open it, just the Name and last name, city and review (no start ratings)

3. Facebook and youtube link

4. Left side below shows 4 slides show with pictures and titles:

1. Kitchen Design

2. Bath Design

3. General Remodeling

4. Commercial Projects

2. About Us:

Our Professionals:

Torvell Builders Project Manager  is responsible to set the project schedule, request materials  and coordinate the delivery on time.  The Project Manager focus is ensuring  the best customer satisfaction in every step of the project until the final product is completed.

The Designer gives you the best ideas in 3D format,   getting the best lay out possible.  understanding your needs, defining your unique style putting together all your requirements and ideas to make the best match for you, making sure you get the best products within your budget

Torvell Builders have a high quality group of trade specialist; plumbers, electricians and installers. Our crew is pleasant to work with,  safety and cleaning values  and very detailed oriented

Our Core Values

As our slogan your project is our business, well we really mean it our job is not just to do the job is to guaranteed a pleasant experience with great costumer service, communication, quality, in time and within your budget

 

1. Services:

1. Commercial

2. Residential

2. Portafolio:  Separated pictures in each project, I want to have a brief description in each picture

1. Kitchen Design

2. Bath Design

3. General Remodeling

4. Commercial Projects

 

1. Contact Us:  

1. Project Management Department:

Contact Person: Rhonda Kestling

Email: rhonda@torvellbuilders.com

2. Office Management Department:

Contact Person: Lou Brambery

Email: info@torvellbuilders.com

 

Please try to pick design style shown in business card to match a little bit. Keep the color tones

I want the logo in the upper left corner and a very nice picture with a kitchen (warm colors)mostly American northeast style like the main pic of the web.

I want the web page is able to be fully open in computers, tablets and cellphones

Please send me an email to torvellbuilders1@mailnest.com so I can send you my logo and any other information to be incorporated

Thank you

Hello Everybody,

Thank you for your time, please make the corrections accordingly:

Pages:

1. Home: Includes a welcome and a briefly say something about our background 

Hello, I just upload my logo and my business card so you can adjust your designs

Please presented responsive format

I want coding the webpage too

Please read carefully my last update

Thank you so much!                                   

Industry/Entity Type

Residential

Requirements
Nice to have
• Should it has a Newsletter subscription with the email at the bottom of the home page
In contact page: A box "Contact us for a free estimate"

```html
<!DOCTYPE html>
<html lang="en">
<head>
<meta charset="utf-8">
<title>Torvell Builders</title>
<link rel="stylesheet" href="https://fonts.googleapis.com/css2?family=Oswald:wght@300;400&family=Open+Sans:wght@400;600&display=swap">
<style>
:root{
  --maroon:#7a2420;
  --maroon-dark:#5e1a17;
  --tan:#e3c48f;
  --tan-light:#f0dcaf;
  --tan-deep:#c79a63;
  --cream:#f3ecd9;
  --rose:#b0605c;
  --panel:#f8f7f5;
  --ink:#3a3330;
  --brown:#6b4a3a;
  --white:#ffffff;
}
*{box-sizing:border-box;margin:0;padding:0}
html,body{width:900px;height:1200px;overflow:hidden}
body{position:relative;background:var(--cream);font-family:"Open Sans",Arial,sans-serif;color:var(--ink)}
.abs{position:absolute}
.top-band{left:0;top:0;width:900px;height:70px;background:var(--tan)}
.header-bar{left:15px;top:14px;width:870px;height:83px;background:var(--maroon);border-radius:4px;box-shadow:0 6px 8px -4px rgba(0,0,0,.25)}
.brand{left:30px;top:0;width:114px;height:114px;border-radius:50%;background:var(--tan);display:flex;align-items:center;justify-content:center;text-align:center;font-family:"Oswald",sans-serif;font-weight:400;font-size:19px;line-height:1.1;color:var(--maroon)}
.tagline{left:152px;top:39px;font-size:22.5px;color:var(--tan)}
.social{top:35px;width:42px;height:42px;border-radius:50%;background:var(--cream)}
.nav{left:15px;top:123px;width:870px;height:44px;background:linear-gradient(#f3dfb2,#e2c183);border:1px solid #d8b77c;border-radius:3px 3px 0 0;display:flex}
.nav a{font-family:"Oswald",sans-serif;font-size:17px;text-decoration:none;color:var(--brown);text-transform:uppercase;height:43px;line-height:43px;text-align:center;border-right:1px solid #cfae78}
.nav a.home{color:var(--maroon)}
.nav a.active{background:var(--maroon);color:var(--tan)}
.dropdown{left:366px;top:167px;width:166px;padding-top:3px;background:var(--maroon);z-index:3}
.dropdown div{height:33px;line-height:33px;padding-left:29px;font-family:"Oswald",sans-serif;font-size:14px;color:var(--tan);border-bottom:1px dotted #a8655a}
.dropdown div.current{background:var(--tan-deep);color:var(--white);border-top:1px dotted var(--tan-light)}
.hero{left:15px;top:167px;width:870px;height:316px;background:linear-gradient(100deg,#d9d2c4 0%,#8a4a32 35%,#6b2f22 55%,#c9b9a0 75%,#e6ddcd 100%)}
.hero-caption{left:15px;top:397px;width:354px;height:52px;background:rgba(227,196,143,.92);font-family:"Oswald",sans-serif;font-size:27px;color:var(--maroon);line-height:52px;padding-left:26px}
.slide-btn{top:439px;width:34px;height:34px;background:var(--maroon);display:flex;align-items:center;justify-content:center}
.welcome{left:15px;top:483px;width:870px;height:228px;background:var(--panel);text-align:center}
.welcome h1{font-family:"Oswald",sans-serif;font-weight:400;font-size:30px;line-height:40px;margin-top:15px;color:var(--ink)}
.welcome h1 span,.welcome em{color:var(--maroon);font-style:normal}
.welcome h2{font-weight:400;font-size:21.5px;line-height:30px;color:#555;margin-top:2px;letter-spacing:.6px}
.divider{width:560px;height:2px;margin:11px auto 12px;background:linear-gradient(90deg,transparent,#cfcfcf,transparent)}
.welcome p{font-size:14px;line-height:20px;color:#555;padding:0 16px;letter-spacing:.1px}
.learn{display:inline-flex;align-items:center;gap:8px;margin-top:12px;font-family:"Oswald",sans-serif;font-weight:300;font-size:20px;color:#6b3a2a}
.card{width:273px;height:186px;background:var(--panel)}
.card h3{height:47px;line-height:50px;padding-left:15px;font-family:"Oswald",sans-serif;font-weight:300;font-size:21px;color:var(--ink)}
.card .photo{position:relative;height:139px}
.card .chev{position:absolute;top:48px}
.card .caption{position:absolute;left:0;bottom:0;width:100%;height:32px;background:rgba(30,30,30,.72);color:var(--white);text-align:center;font-size:17px;line-height:32px}
.reviews{left:613px;top:724px;width:272px;height:378px;background:var(--rose)}
.reviews h3{height:47px;line-height:50px;padding-left:18px;font-family:"Oswald",sans-serif;font-weight:300;font-size:22px;color:#f5e6d0;border-bottom:1px solid #d79a94}
.review{position:relative;padding-left:18px;color:var(--white);font-size:16px;border-bottom:1px solid #d79a94}
.review .toggle{position:absolute;right:10px;width:20px;height:20px;border-radius:50%;background:#f5ece5;color:var(--rose);font-weight:600;font-size:17px;line-height:19px;text-align:center}
.review.open{background:var(--tan);color:var(--maroon)}
.review.open p{color:var(--ink);font-size:13px;line-height:19px;margin-top:4px}
.review.open .more{position:absolute;right:19px;bottom:9px;font-size:11px;color:var(--maroon);text-decoration:underline}
.footer{left:0;top:1116px;width:900px;height:84px;background:var(--maroon);color:var(--white);font-size:13px}
.footer .links{position:absolute;left:15px;top:24px}
.footer .copy{position:absolute;left:15px;top:47px}
.newsletter{position:absolute;left:623px;top:12px;display:flex;align-items:center;gap:8px;font-size:13px;letter-spacing:.5px}
.signup{position:absolute;left:620px;top:38px;width:267px;height:33px;background:#2a0d0b;border-radius:5px;padding:2px;display:flex}
.signup .field{flex:1;background:var(--white);border-radius:4px 0 0 4px;color:#aaa;font-size:14px;line-height:29px;padding-left:10px}
.signup .join{width:68px;background:linear-gradient(#f0d9a6,#d9b472);border-radius:0 4px 4px 0;color:var(--maroon);font-family:"Oswald",sans-serif;font-size:16px;text-align:center;line-height:29px}
</style>
</head>
<body>
<div class="abs top-band"></div>
<div class="abs header-bar"></div>
<div class="abs brand">Torvell<br>Builders</div>
<div class="abs tagline">Your project is our business</div>
<a class="abs social" style="left:767px" aria-label="Social page"></a>
<a class="abs social" style="left:827px" aria-label="Video channel"></a>

<nav class="abs nav">
  <a class="home" style="width:98px">Home</a><a style="width:127px">About Us</a><a style="width:126px">Services</a><a class="active" style="width:139px">Portafolio</a><a style="width:151px">Contact Us</a>
</nav>

<div class="abs hero" role="img" aria-label="Warm kitchen with wood cabinets, island and bar stools"></div>
<div class="abs dropdown">
  <div>Kitchen Design</div><div class="current">Bath Design</div><div>General Remodeling</div><div>Commercial Projects</div>
</div>
<div class="abs hero-caption">LOREM IPSUM &amp; DOLOR AMET!</div>
<div class="abs slide-btn" style="left:796px"><svg width="12" height="18"><path d="M9 2 3 9l6 7" stroke="#fff" stroke-width="3" fill="none"/></svg></div>
<div class="abs slide-btn" style="left:836px"><svg width="12" height="18"><path d="M3 2l6 7-6 7" stroke="#fff" stroke-width="3" fill="none"/></svg></div>

<section class="abs welcome">
  <h1>Welcome to <span>Torvell Builders</span> Website</h1>
  <h2>simply dummy text of the printing and typesetting.</h2>
  <div class="divider"></div>
  <p>It is a long established fact that a reader will be <em>distracted</em> by the readable content of a page when looking at its layout. tthat a reader will be <em>distracted</em> by the readable content of a page when looking at its layout. The point of using Lorem Ipsum is that it has a more-or-less as opposed to using '<em>Content here, content here</em>',</p>
  <div class="learn">learn more <svg width="20" height="20"><circle cx="10" cy="10" r="9" fill="#6b3a2a"/><path d="M5 10h9M10 6l4 4-4 4" stroke="#fff" stroke-width="2" fill="none"/></svg></div>
</section>

<div class="abs card" style="left:15px;top:724px"><h3>KITCHEN DESIGN</h3>
  <div class="photo" role="img" aria-label="Kitchen with dark wood cabinets and red tile backsplash" style="background:linear-gradient(90deg,#5a3322,#9a5a38,#4a2a1e)">
    <svg class="chev" style="left:6px" width="14" height="28"><path d="M11 2 3 14l8 12" stroke="#fff" stroke-width="2" fill="none"/></svg>
    <svg class="chev" style="right:6px" width="14" height="28"><path d="M3 2l8 12-8 12" stroke="#fff" stroke-width="2" fill="none"/></svg>
    <div class="caption">Variations of Passages</div></div></div>
<div class="abs card" style="left:315px;top:724px"><h3>BATH DESIGN</h3>
  <div class="photo" role="img" aria-label="White bathroom with toilet and bathtub" style="background:linear-gradient(90deg,#8a8580,#dcd8d2,#c9c4bd)">
    <svg class="chev" style="left:4px" width="14" height="28"><path d="M11 2 3 14l8 12" stroke="#7a2420" stroke-width="3" fill="none"/></svg>
    <svg class="chev" style="right:4px" width="14" height="28"><path d="M3 2l8 12-8 12" stroke="#7a2420" stroke-width="3" fill="none"/></svg>
    <div class="caption">Specimen Book</div></div></div>
<div class="abs card" style="left:15px;top:916px"><h3>GENERAL REMODELING</h3>
  <div class="photo" role="img" aria-label="Workers building cabinetry in a remodel" style="background:linear-gradient(90deg,#c9a77a,#8a6a52,#d8c3a0)">
    <svg class="chev" style="left:6px" width="14" height="28"><path d="M11 2 3 14l8 12" stroke="#fff" stroke-width="2" fill="none"/></svg>
    <svg class="chev" style="right:6px" width="14" height="28"><path d="M3 2l8 12-8 12" stroke="#7a2420" stroke-width="3" fill="none"/></svg>
    <div class="caption">Variations of Passages</div></div></div>
<div class="abs card" style="left:315px;top:916px"><h3>COMMERCIAL PROJECTS</h3>
  <div class="photo" role="img" aria-label="Office lounge with blue sofas" style="background:linear-gradient(90deg,#b5aa98,#6a7ea8,#c7bca8)">
    <svg class="chev" style="left:4px" width="14" height="28"><path d="M11 2 3 14l8 12" stroke="#7a2420" stroke-width="3" fill="none"/></svg>
    <svg class="chev" style="right:4px" width="14" height="28"><path d="M3 2l8 12-8 12" stroke="#7a2420" stroke-width="3" fill="none"/></svg>
    <div class="caption">Specimen Book</div></div></div>

<aside class="abs reviews">
  <h3>REVIEWS</h3>
  <div class="review" style="height:44px;line-height:43px">Wade Pellow - NY<span class="toggle" style="top:12px">+</span></div>
  <div class="review open" style="height:101px;padding-top:11px">Nora Fenwick - NY<span class="toggle" style="top:13px">-</span>
    <p>Lorem ipsum dolor sit amet conse<br>ctetur adipisicing elit,</p><span class="more">Read more</span></div>
  <div class="review" style="height:43px;line-height:42px">Colin Hatcher - NY<span class="toggle" style="top:11px">+</span></div>
  <div class="review" style="height:44px;line-height:43px">Ty Ormond - NY<span class="toggle" style="top:12px">+</span></div>
  <div class="review" style="height:47px;line-height:46px">Darnell Whitlow - NY<span class="toggle" style="top:13px">+</span></div>
  <div class="review" style="height:52px;line-height:48px;border-bottom:none">Nora Fenwick - NY<span class="toggle" style="top:14px">+</span></div>
</aside>

<footer class="abs footer">
  <div class="links">Home | About Us | Services | Portafolio | Contact Us</div>
  <div class="copy">Torvell Builders © 2014. Privacy Policy</div>
  <div class="newsletter"><svg width="27" height="19"><rect x="1" y="1" width="25" height="17" fill="#fff"/><path d="M1 1l12.5 10L26 1" stroke="#7a2420" stroke-width="2" fill="none"/></svg>SUBSCRIBE TO OUR NEWSLETTER</div>
  <div class="signup"><div class="field">yourname@email.com</div><div class="join">Join</div></div>
</footer>
</body>
</html>
```